Corvana Dental Development - Business Cards

We are a Dental Development and Management company. We are looking to develop a new business card design. We are business professional but modern. The logo that I have attached is the business colors. You can also check out our website for further detail. www.corvanadentalmanagement.example

Target Market(s)

Dental Professionals, Dentists and Office Staff, Marketing Professionals

Industry/Entity Type

Business

Requirements
Must have
• Name - Dominic R. Hartwell
Title - Marketing Director
Phone - 555-014-2273
Cell - 555-014-2273
Email - Dom.h@Corvanadentaldevelopment.example
Address - 2918 W Larkspur Rd, Mesa, AZ 85213
Web- www.corvanadentaldevelopment.example

Corvana Logo must go on the front. The other logos go on the back as affiliated businesses

Must be editable to enter specific Names, Positions, Phone numbers and email later on. Using Adobe CS5 currently.

```html
<!DOCTYPE html>
<html lang="en">
<head>
<meta charset="utf-8">
<title>Corvana Dental Development – Business Cards</title>
<link rel="stylesheet" href="https://fonts.googleapis.com/css2?family=Lato:wght@400;700&display=swap">
<style>
  :root {
    --backdrop: #dfe3e6;
    --card: #ffffff;
    --panel: #ebeaf3;
    --panel-edge: #dcdbe9;
    --brand-navy: #3d3b70;
    --brand-gold: #d29b32;
    --ink: #333338;
    --plan-red: #a3222b;
    --centers-blue: #2f5f86;
    --kids-purple: #6a2d8f;
    --urgent-red: #e0282e;
    --urgent-blue: #3b3d8f;
  }
  * { box-sizing: border-box; margin: 0; padding: 0; }
  html, body { width: 1200px; height: 960px; overflow: hidden; }
  body {
    background: var(--backdrop);
    font-family: "Lato", Arial, sans-serif;
    color: var(--ink);
    position: relative;
  }
  .card {
    position: absolute;
    left: 250px;
    width: 700px;
    height: 400px;
    background: var(--card);
    box-shadow: 0 6px 18px rgba(0,0,0,.15);
    overflow: hidden;
  }
  .card--front { top: 40px; }
  .card--back { top: 520px; }
  .card__panel { position: absolute; inset: 0; width: 100%; height: 100%; }

  .brand {
    position: absolute;
    left: 60px; top: 58px;
    display: flex; align-items: center; gap: 14px;
  }
  .brand__dot { width: 22px; height: 22px; border-radius: 50%; background: var(--brand-gold); }
  .brand__name {
    font-size: 30px; font-weight: 700; color: var(--brand-navy);
    letter-spacing: .5px;
  }

  .person { position: absolute; left: 60px; top: 168px; }
  .person__name { font-size: 30px; font-weight: 400; color: var(--ink); }
  .person__title {
    margin-top: 6px; font-size: 20px; color: var(--brand-navy);
    text-transform: uppercase; letter-spacing: .5px;
  }
  .divider {
    position: absolute; left: 60px; top: 252px;
    width: 400px; height: 2px; background: var(--brand-navy);
  }
  .contacts { position: absolute; left: 60px; top: 266px; list-style: none; }
  .contacts li {
    display: flex; align-items: center; gap: 10px;
    font-size: 18px; height: 27px;
  }
  .contacts svg { width: 18px; height: 18px; fill: var(--brand-navy); flex: none; }
  .contacts .phones { gap: 10px; }
  .contacts .phones span + svg { margin-left: 16px; }
  .contacts .web { font-weight: 700; color: var(--brand-navy); }

  .affiliates {
    position: absolute; inset: 0;
    display: grid; grid-template-columns: 1fr 1fr; grid-template-rows: 1fr 1fr;
    padding: 50px 40px;
  }
  .affiliate {
    display: flex; align-items: center; justify-content: center; gap: 12px;
    font-size: 26px; font-weight: 700; text-align: center; line-height: 1.15;
  }
  .affiliate--plan { color: var(--plan-red); }
  .affiliate--centers { color: var(--centers-blue); }
  .affiliate--kids { color: var(--kids-purple); }
  .affiliate--urgent { color: var(--urgent-blue); }
  .affiliate__mark { width: 34px; height: 34px; background: var(--urgent-red); flex: none; }
</style>
</head>
<body>

<section class="card card--front" aria-label="Business card front">
  <svg class="card__panel" viewBox="0 0 700 400" preserveAspectRatio="none" aria-hidden="true">
    <defs>
      <linearGradient id="panelFront" x1="0" x2="1">
        <stop offset="0" stop-color="#f4f3f9"/>
        <stop offset="1" stop-color="#e6e5f0"/>
      </linearGradient>
    </defs>
    <path d="M440 0 Q350 190 390 400 L700 400 L700 0 Z" fill="url(#panelFront)"/>
  </svg>

  <div class="brand">
    <span class="brand__dot"></span>
    <span class="brand__name">Corvana Dental Development</span>
  </div>

  <div class="person">
    <p class="person__name">Dominic R. Hartwell</p>
    <p class="person__title">Marketing Director</p>
  </div>
  <div class="divider"></div>

  <ul class="contacts">
    <li class="phones">
      <svg viewBox="0 0 24 24"><path d="M4 3h6v18H4zM12 8h8v13h-8zM14 10v2h4v-2zM14 14v2h4v-2z"/></svg>
      <span>555-014-2273</span>
      <svg viewBox="0 0 24 24"><path d="M7 1h10a1 1 0 0 1 1 1v20a1 1 0 0 1-1 1H7a1 1 0 0 1-1-1V2a1 1 0 0 1 1-1zm1 3v12h8V4zm4 14a1.5 1.5 0 1 0 0 3 1.5 1.5 0 0 0 0-3z"/></svg>
      <span>555-014-2273</span>
    </li>
    <li>
      <svg viewBox="0 0 24 24"><path d="M2 5h20v14H2zm2 2v.5l8 5.5 8-5.5V7zm0 3v7h16v-7l-8 5.5z"/></svg>
      <span>Dom.h@Corvanadentaldevelopment.example</span>
    </li>
    <li>
      <svg viewBox="0 0 24 24"><path d="M12 1a7 7 0 0 0-7 7c0 5.3 7 15 7 15s7-9.7 7-15a7 7 0 0 0-7-7zm0 9.5A2.5 2.5 0 1 1 12 5.5a2.5 2.5 0 0 1 0 5z"/></svg>
      <span>2918 W Larkspur Rd, Mesa, AZ 85213</span>
    </li>
    <li>
      <svg viewBox="0 0 24 24"><path d="M12 2a10 10 0 1 0 0 20 10 10 0 0 0 0-20zm-1 17.9A8 8 0 0 1 4.1 11H8c.2 2.8 1.2 5.5 3 8.9zM8 9H4.1A8 8 0 0 1 11 4.1C9.2 7.5 8.2 8 8 9zm5 10.9c1.8-3.4 2.8-6.1 3-8.9h3.9a8 8 0 0 1-6.9 8.9zM16 9c-.2-1-1.2-1.5-3-4.9A8 8 0 0 1 19.9 9zm-6 0c.3-1.6 1-3.3 2-5 1 1.7 1.7 3.4 2 5zm0 2h4c-.3 2-1 4.2-2 6.5-1-2.3-1.7-4.5-2-6.5z"/></svg>
      <span class="web">www.corvanadentaldevelopment.example</span>
    </li>
  </ul>
</section>

<section class="card card--back" aria-label="Business card back, affiliated businesses">
  <svg class="card__panel" viewBox="0 0 700 400" preserveAspectRatio="none" aria-hidden="true">
    <defs>
      <linearGradient id="panelBack" x1="0" x2="1">
        <stop offset="0" stop-color="#f5f4fa"/>
        <stop offset="1" stop-color="#e4e3ee"/>
      </linearGradient>
    </defs>
    <path d="M390 0 Q270 180 330 400 L700 400 L700 0 Z" fill="url(#panelBack)"/>
  </svg>

  <div class="affiliates">
    <div class="affiliate affiliate--plan">Hearthside Dental Plan</div>
    <div class="affiliate affiliate--centers">Hearthside Dental Centers</div>
    <div class="affiliate affiliate--kids">Brightbloom Pediatric Dental</div>
    <div class="affiliate affiliate--urgent"><span class="affiliate__mark"></span>Rapidcare Dental Centers</div>
  </div>
</section>

</body>
</html>
```